Website Redesign For Motorbike Rental Company In Thailand

We are a motorbike rental start up in Phuket, Thailand named RIDE ON.

We cater to the tourist and even ex pats that want to rent a motorbike for as short as only 3 days up to 1 year at a time.

We want a website that makes it a very simple ordering process for the customer. Be able to order a motorbike rental without scrolling down...

Simple, attractive design that builds trust and credibility is huge.

Please check this google doc for the CONTENT: https://files.velmora-docs.example/sheet/7KqT2wXbRn4LpZ9cYmHfJd3sVa8GtEu1NoBiQrWk/view?mode=share

Target Market(s)

Tourists In Thailand & Expats In Thailand

Industry/Entity Type

motorbike rental, motorcycle rental

Number of Pages Required

1 page

Requirements
Must have
• Must have a thailand phuket theme or feel
Nice to have
• We want a website that makes it a very simple ordering process for the customer. Be able to order a motorbike rental without scrolling down... Simple, attractive design that builds trust and credibility is huge.
Should not have
• na

```html
<!DOCTYPE html>
<html lang="en">
<head>
<meta charset="utf-8">
<title>RIDE ON – Motorbike Rentals in Phuket</title>
<link rel="stylesheet" href="https://fonts.googleapis.com/css2?family=Montserrat:wght@400;500;600;700;800&display=swap">
<style>
:root{
  --orange:#f47a1f;
  --orange-dark:#e06a10;
  --ink:#1d1d1d;
  --muted:#8a8a8a;
  --line:#e6e6e6;
  --soft:#f6f6f6;
  --white:#ffffff;
  --hero-a:#2a2a2c;
  --hero-b:#5b5d61;
}
*{box-sizing:border-box;margin:0;padding:0}
html,body{width:1200px;height:4173px;overflow:hidden}
body{position:relative;background:var(--white);font-family:'Montserrat',sans-serif;color:var(--ink)}

/* presentation header */
.brand-band{position:absolute;left:0;top:0;width:1200px;height:615px;background:var(--orange);display:flex;flex-direction:column;align-items:center;padding-top:92px}
.brand-band .brand-name{font-size:76px;font-weight:800;color:var(--white);letter-spacing:2px;line-height:1}
.brand-band .brand-tag{margin-top:16px;font-size:12px;font-weight:700;color:var(--white);letter-spacing:1px}
.section-label{position:absolute;left:0;width:1200px;top:930px;text-align:center;font-size:26px;font-weight:400;letter-spacing:26px;padding-left:26px}

/* shared */
.page{position:absolute;background:var(--white);box-shadow:0 2px 14px rgba(0,0,0,.08);overflow:hidden}
.logo{display:flex;align-items:center;gap:5px;font-weight:800;color:var(--ink)}
.logo .dot{width:12px;height:12px;border-radius:50%;background:var(--orange)}
.socials{display:flex;gap:5px}
.socials span{width:11px;height:11px;border-radius:50%;background:var(--orange)}
.btn{background:var(--orange);color:var(--white);font-weight:700;text-align:center;display:block}

/* ===== desktop ===== */
.desk{left:104px;top:1030px;width:726px;height:2637px}
.desk .nav{height:54px;display:flex;align-items:center;padding:0 77px;justify-content:space-between}
.desk .nav .logo{font-size:14px}
.desk .nav ul{display:flex;gap:17px;list-style:none;font-size:6.5px;color:#555;margin-left:60px}
.desk .hero{position:absolute;top:56px;left:0;width:726px;height:358px;background:linear-gradient(110deg,var(--hero-a) 0%,#3c3d40 45%,var(--hero-b) 100%)}
.desk .hero h1{position:absolute;left:77px;top:62px;color:var(--white);font-size:27px;font-weight:800;line-height:1.2;width:300px}
.desk .hero ul{position:absolute;left:77px;top:170px;list-style:none;color:#e9e9e9;font-size:7px;line-height:18px}
.desk .hero li::before{content:"•";margin-right:5px}
.bookcard{position:absolute;background:var(--white);box-shadow:0 4px 16px rgba(0,0,0,.12);text-align:center}
.desk .bookcard{left:420px;top:145px;width:232px;height:386px;padding:16px 14px}
.steps{display:flex;justify-content:space-around;font-weight:700;color:#ccc;border-bottom:1px solid var(--line)}
.steps .on{color:var(--orange);border-bottom:2px solid var(--orange)}
.desk .steps{font-size:8px;padding-bottom:8px}
.bookcard h3{font-weight:700}
.desk .bookcard h3{font-size:10px;margin:27px 0 8px}
.select{border:1px solid var(--line);margin:0 auto;text-align:left;color:var(--muted)}
.desk .select{width:84px;height:14px;font-size:5.5px;padding:3px 5px}
.bikeview{position:relative;margin:0 auto;border:1px solid var(--line)}
.desk .bikeview{width:176px;height:112px;margin-top:6px}
.bikeview .ph{position:absolute;background:radial-gradient(ellipse at center,#4a5f82 0%,#2b3548 45%,rgba(255,255,255,0) 72%)}
.desk .bikeview .ph{left:28px;top:6px;width:120px;height:100px}
.arrow{position:absolute;top:50%;width:14px;height:14px;margin-top:-7px;border-radius:50%;background:var(--white);box-shadow:0 1px 4px rgba(0,0,0,.2);font-size:8px;line-height:14px;text-align:center}
.desk .bookcard h4{font-size:8.5px;font-weight:800;margin:15px 0 8px}
.fields{display:grid;grid-template-columns:1fr 1fr;gap:4px}
.fields div{border:1px solid var(--line);text-align:left;color:var(--muted)}
.fields .full{grid-column:1 / 3}
.desk .fields div{height:16px;font-size:5px;padding:4px 5px}
.desk .fields .area{height:24px}
.desk .bookcard .btn{width:62px;height:15px;font-size:5.5px;line-height:15px;margin:10px auto 0}
.desk .callbox{position:absolute;left:77px;top:428px;width:329px;height:104px;background:var(--orange);color:var(--white);text-align:center;padding-top:26px}
.desk .callbox b{display:block;font-size:18px;font-weight:700}
.desk .callbox span{display:block;font-size:14px;margin-top:10px;letter-spacing:.5px}
.desk h2{font-weight:800;font-size:18.5px}
.desk .cities-h{position:absolute;left:77px;top:589px;width:520px;font-size:18.5px;line-height:1.3}
.desk .cities{position:absolute;left:77px;top:667px;width:575px;height:134px;box-shadow:0 2px 10px rgba(0,0,0,.08);padding:12px 10px;display:grid;grid-template-columns:repeat(4,1fr);grid-auto-rows:30px;gap:10px 13px}
.city{display:flex;align-items:center;border:1px solid var(--line);height:30px;font-size:7px}
.city::before{content:"";flex:none;width:7px;height:7px;border-radius:50%;background:var(--orange);margin:0 16px 0 12px}
.desk .how{position:absolute;top:816px;left:0;width:726px;height:370px;background:var(--soft)}
.center-h{text-align:center}
.desk .how h2{margin-top:54px}
.cols3{position:absolute;left:77px;width:575px;display:grid;grid-template-columns:repeat(3,183px);gap:13px}
.desk .how .cols3{top:108px}
.step-card{position:relative;text-align:center}
.step-card .ph{height:121px}
.step-card .num{position:absolute;top:-9px;left:12px;width:18px;height:18px;border-radius:50%;background:var(--white);border:2px solid var(--orange);font-size:7px;font-weight:700;line-height:14px}
.step-card p{font-size:10px;font-weight:700;margin-top:24px;line-height:1.4;padding:0 20px}
.desk .bikes{position:absolute;top:1186px;left:0;width:726px;height:470px}
.desk .bikes h2{margin-top:58px}
.desk .bikes .cols3{top:112px}
.bike{text-align:center}
.bike .frame{height:148px;border:1px solid var(--line);position:relative}
.bike .frame .ph{position:absolute;left:28px;top:14px;width:126px;height:120px}
.bike h5{font-size:13px;font-weight:500;margin-top:25px}
.bike p{font-size:8px;color:#666;line-height:16px;margin-top:5px}
.bike .btn{width:100px;height:22px;font-size:6px;line-height:22px;margin:14px auto 0}
.desk .bikes .arrow.l{left:70px;top:186px}
.desk .bikes .arrow.r{left:642px;top:186px}
.desk .news{position:absolute;top:1656px;left:0;width:726px;height:722px;background:var(--soft)}
.desk .news h2{position:absolute;left:77px;top:54px}
.desk .news .grid{position:absolute;left:77px;top:105px;width:575px;display:grid;grid-template-columns:repeat(3,183px);gap:40px 13px}
.post .ph{height:123px}
.post h6{font-size:8px;font-weight:700;margin-top:25px;line-height:1.45}
.post .date{font-size:6px;color:var(--orange);font-weight:600;margin-top:2px}
.post p{font-size:5.5px;color:#777;line-height:1.6;margin-top:12px}
.post .more{font-size:5.5px;color:var(--orange);font-weight:600;margin-top:12px;display:flex;align-items:center;gap:6px}
.post .more::after{content:"";width:26px;height:1px;background:var(--orange)}
.desk .foot{position:absolute;top:2378px;left:0;width:726px;height:259px}
.desk .foot .logo{position:absolute;left:77px;top:66px;font-size:24px}
.desk .foot .blurb{position:absolute;left:77px;top:162px;width:190px;font-size:5.5px;color:#777;line-height:1.6}
.desk .foot ul{position:absolute;right:75px;top:86px;display:flex;gap:20px;list-style:none;font-size:6px;color:#555}
.desk .foot .copy{position:absolute;right:75px;top:117px;width:200px;text-align:right;font-size:5.5px;color:#777;line-height:1.6}
.desk .foot .socials{position:absolute;right:75px;top:143px}

/* ===== mobile ===== */
.mob{left:904px;top:1030px;width:188px;height:2995px}
.mob .nav{height:45px;display:flex;align-items:center;justify-content:space-between;padding:0 10px}
.mob .nav .logo{font-size:11px}
.mob .nav .right{display:flex;align-items:center;gap:8px}
.mob .nav .socials span{width:8px;height:8px}
.burger{width:18px;height:9px;border-top:1.5px solid var(--ink);border-bottom:1.5px solid var(--ink);position:relative}
.burger::after{content:"";position:absolute;left:0;right:0;top:2.5px;border-top:1.5px solid var(--ink)}
.mob .hero{position:absolute;top:45px;left:0;width:188px;height:330px;background:linear-gradient(160deg,var(--hero-a),var(--hero-b))}
.mob .hero h1{position:absolute;left:10px;top:42px;color:var(--white);font-size:19px;font-weight:800;line-height:1.17}
.mob .hero ul{position:absolute;left:10px;top:148px;list-style:none;color:#e6e6e6;font-size:5.5px;line-height:15px}
.mob .hero li::before{content:"•";margin-right:4px}
.mob .bookcard{left:38px;top:328px;width:148px;height:290px;padding:12px 8px}
.mob .steps{font-size:5.5px;padding-bottom:5px}
.mob .bookcard h3{font-size:7px;margin:20px 0 5px}
.mob .select{width:56px;height:10px;font-size:4px;padding:2px 3px}
.mob .bikeview{width:132px;height:86px;margin-top:5px;border:none}
.mob .bikeview .ph{left:20px;top:2px;width:92px;height:82px}
.mob .arrow{width:10px;height:10px;margin-top:-5px;font-size:6px;line-height:10px}
.mob .bookcard h4{font-size:6px;font-weight:800;margin:10px 0 6px}
.mob .fields{gap:3px}
.mob .fields div{height:11px;font-size:3.5px;padding:3px}
.mob .fields .area{height:16px}
.mob .bookcard .btn{width:44px;height:11px;font-size:4px;line-height:11px;margin:8px auto 0}
.mob .callbox{position:absolute;left:10px;top:625px;width:176px;height:88px;background:var(--orange);color:var(--white);text-align:center;padding-top:27px}
.mob .callbox b{display:block;font-size:13px}
.mob .callbox span{display:block;font-size:10px;margin-top:7px}
.mob h2{font-weight:800;font-size:13.5px;line-height:1.3}
.mob .cities-h{position:absolute;left:10px;top:747px;width:160px;font-size:13.5px}
.mob .cities{position:absolute;left:10px;top:862px;display:flex;flex-direction:column;gap:14px}
.mob .city{width:130px;height:26px;font-size:6px;border:1px solid var(--line)}
.mob .city::before{margin:0 12px 0 10px;width:6px;height:6px}
.mob .how{position:absolute;top:1353px;left:0;width:188px;height:748px;background:var(--soft)}
.mob .how h2{margin-top:60px}
.mob .how .stack{position:absolute;left:10px;top:110px;width:172px;display:flex;flex-direction:column}
.mob .step-card{height:211px}
.mob .step-card .ph{height:114px}
.mob .step-card .num{width:16px;height:16px;font-size:6px;line-height:12px}
.mob .step-card p{font-size:9px;margin-top:18px;padding:0 10px}
.mob .bikes{position:absolute;top:2101px;left:0;width:188px;height:335px;overflow:hidden}
.mob .bikes h2{margin-top:42px}
.mob .bikes .row{position:absolute;left:10px;top:82px;display:flex;gap:10px}
.mob .bike{width:156px;flex:none}
.mob .bike .frame{height:128px}
.mob .bike .frame .ph{left:20px;top:12px;width:116px;height:104px}
.mob .bike h5{font-size:10px;margin-top:18px}
.mob .bike p{font-size:6px;line-height:12px}
.mob .bike .btn{width:76px;height:17px;font-size:4.5px;line-height:17px;margin-top:10px}
.mob .news{position:absolute;top:2436px;left:0;width:188px;height:323px;background:var(--soft);overflow:hidden}
.mob .news h2{position:absolute;left:10px;top:36px}
.mob .news .row{position:absolute;left:10px;top:90px;display:flex;gap:10px}
.mob .post{width:146px;flex:none}
.mob .post .ph{height:97px}
.mob .post h6{font-size:6px;margin-top:8px}
.mob .post .date{font-size:4.5px}
.mob .post p{font-size:4px;margin-top:4px}
.mob .post .more{font-size:4px;margin-top:8px}
.mob .post .more::after{width:20px}
.mob .foot{position:absolute;top:2759px;left:0;width:188px;height:236px;padding:0 10px}
.mob .foot .logo{margin-top:58px;font-size:16px}
.mob .foot .blurb{font-size:4.5px;color:#777;line-height:1.6;margin-top:18px;width:150px}
.mob .foot ul{display:flex;flex-wrap:wrap;gap:4px 14px;list-style:none;font-size:4.5px;color:#555;margin-top:20px;width:170px}
.mob .foot .copy{font-size:4.5px;color:#777;margin-top:12px;line-height:1.6}
.mob .foot .socials{margin-top:8px}
.mob .foot .socials span{width:8px;height:8px}
</style>
</head>
<body>

<header class="brand-band">
  <div class="brand-name">RIDE ON</div>
  <div class="brand-tag">MOTORBIKES FOR RENT IN PHUKET</div>
</header>

<div class="section-label">HOMEPAGE</div>

<!-- desktop homepage -->
<main class="page desk">
  <nav class="nav">
    <div class="logo"><span class="dot"></span>RIDE ON</div>
    <ul><li>Home</li><li>Deliver</li><li>How It Works</li><li>Booking Process</li><li>Popular Bikes</li><li>Blogs</li></ul>
    <div class="socials"><span></span><span></span><span></span></div>
  </nav>

  <section class="hero" role="img" aria-label="Row of rental motorbikes parked along a street, darkened">
    <h1>Fast Motorbike Rentals In Phuket, Thailand</h1>
    <ul>
      <li>Free Delivery &amp; Pick Up Anywhere In Phuket</li>
      <li>Free High Quality Helmet Included</li>
      <li>Free Unlimited Mileage</li>
      <li>Easy &amp; Quick Online Booking</li>
      <li>No Credit Card Required</li>
      <li>Pay When Bike Is Delivered</li>
      <li>Speak English &amp; Thai</li>
    </ul>
  </section>

  <div class="callbox"><b>You Can Call Us</b><span>123-456-7890</span></div>

  <form class="bookcard">
    <div class="steps"><span class="on">Step 1</span><span>Step 2</span><span>Step 3</span></div>
    <h3>Choose Your Bike</h3>
    <div class="select">Vendor &nbsp;&nbsp;&nbsp;&nbsp;&nbsp;&nbsp;&nbsp;&nbsp;&nbsp;&nbsp;&nbsp;&nbsp;&nbsp;&nbsp;&nbsp;&nbsp; ▾</div>
    <div class="bikeview">
      <div class="ph" role="img" aria-label="Blue scooter"></div>
      <span class="arrow" style="left:-7px">‹</span>
      <span class="arrow" style="right:-7px">›</span>
    </div>
    <h4>ENTER YOUR DETAILS</h4>
    <div class="fields">
      <div>Name</div><div>Phone Number</div>
      <div class="full">Email</div>
      <div class="full">Messaging ID</div>
      <div class="full area">Location</div>
    </div>
    <span class="btn">Next</span>
  </form>

  <h2 class="cities-h">We Deliver Motorbikes and Scooters To These Cities In Phuket, Thailand</h2>
  <div class="cities">
    <div class="city">Cherng Talay</div><div class="city">Bangtao</div><div class="city">Chalong</div><div class="city">Kamala</div>
    <div class="city">Karon</div><div class="city">Kata</div><div class="city">Kathu</div><div class="city">Nai Harn</div>
    <div class="city">Patong</div><div class="city">Phuket Town</div><div class="city">Rawai</div><div class="city">Mai Khao</div>
  </div>

  <section class="how">
    <h2 class="center-h">How It Works</h2>
    <div class="cols3">
      <div class="step-card"><div class="ph" role="img" aria-label="Grey scooter parked on a street" style="background:linear-gradient(#8a9aa6,#3d4148)"></div><span class="num">1</span><p>Choose Your Bike</p></div>
      <div class="step-card"><div class="ph" role="img" aria-label="Hand signing a rental form" style="background:linear-gradient(135deg,#e9ecef,#9fb2c6)"></div><span class="num">2</span><p>Enter Rental Date Period &amp; Enter Delivery Address Or Choose To Pick Up</p></div>
      <div class="step-card"><div class="ph" role="img" aria-label="Two travellers riding a scooter" style="background:linear-gradient(135deg,#7f6b5a,#c8b9a6)"></div><span class="num">3</span><p>Get Your Bike Delivered In Less Than 2 Hours Or Pick Up ASAP!</p></div>
    </div>
  </section>

  <section class="bikes">
    <h2 class="center-h">Popular Bikes</h2>
    <span class="arrow l">‹</span><span class="arrow r">›</span>
    <div class="cols3">
      <div class="bike"><div class="frame"><div class="ph" role="img" aria-label="Grey and black scooter" style="background:radial-gradient(ellipse,#4b4f55 0%,#8a8f96 40%,rgba(255,255,255,0) 70%)"></div></div>
        <h5>Kito-Glide</h5><p>120 Km/H or 75 Mph<br>200 Baht/Day<br>58.8 km/L or 138 MPG</p><span class="btn">Booking</span></div>
      <div class="bike"><div class="frame"><div class="ph" role="img" aria-label="Blue scooter" style="background:radial-gradient(ellipse,#1f5fb3 0%,#5e8fd0 40%,rgba(255,255,255,0) 70%)"></div></div>
        <h5>Kito-Cruz</h5><p>115 Km/H or 71 Mph<br>225 Baht/Day<br>43.3 km/l or 101.83 mpg</p><span class="btn">Booking</span></div>
      <div class="bike"><div class="frame"><div class="ph" role="img" aria-label="Black maxi scooter" style="background:radial-gradient(ellipse,#222 0%,#666 40%,rgba(255,255,255,0) 70%)"></div></div>
        <h5>Maro-TX</h5><p>160 Km/H or 100 Mph<br>1000 Baht/Day<br>20.0 km/l or 47.04 mpg</p><span class="btn">Booking</span></div>
    </div>
  </section>

  <section class="news">
    <h2>Latest News &amp; Blogs</h2>
    <div class="grid">
      <article class="post"><div class="ph" role="img" aria-label="Riders on scooters at a checkpoint" style="background:linear-gradient(135deg,#6d7a5c,#b9b4a2)"></div>
        <h6>The Penalties for Traffic Offenses in Thailand</h6><div class="date">2021-02-03</div>
        <p>Many people riding in Thailand are not aware of the local traffic rules. The most common offenses among tourists include riding without a helmet or licence.</p><div class="more">Read more</div></article>
      <article class="post"><div class="ph" role="img" aria-label="Packing list items for a motorbike trip" style="background:linear-gradient(135deg,#d6e8f2,#4f9ad1)"></div>
        <h6>What to Take with You on a Motorcycle Trip in Thailand</h6><div class="date">2021-02-03</div>
        <p>Renting a scooter in Thailand is one of the most popular ways to explore the Land of Smiles. A scooter gives you freedom and the road.</p><div class="more">Read more</div></article>
      <article class="post"><div class="ph" role="img" aria-label="Row of parked scooters" style="background:linear-gradient(135deg,#59606a,#a8b0b9)"></div>
        <h6>Why Choose Long-Term Motorcycle Rentals over Purchasing</h6><div class="date">2021-02-03</div>
        <p>Long-term rental is popular in Europe and the United States. Renting a vehicle instead of buying one can have a lot of advantages. If you...</p><div class="more">Read more</div></article>
      <article class="post"><div class="ph" role="img" aria-label="Dirt bike on a forest trail" style="background:linear-gradient(135deg,#4d6b3a,#a79a7a)"></div>
        <h6>Enduro Ride in Kamala</h6><div class="date">2021-02-03</div>
        <p>Lorem ipsum is simply dummy text of the printing and typesetting industry. Lorem ipsum has been the industry's standard dummy text ever since the 1500s.</p><div class="more">Read more</div></article>
      <article class="post"><div class="ph" role="img" aria-label="Coastal viewpoint over the sea" style="background:linear-gradient(180deg,#9cc3d6,#5f8b74)"></div>
        <h6>Black Rock Viewpoint – Enduro Ride</h6><div class="date">2021-02-03</div>
        <p>Lorem ipsum is simply dummy text of the printing and typesetting industry. Lorem ipsum has been the industry's standard dummy text ever since the 1500s.</p><div class="more">Read more</div></article>
      <article class="post"><div class="ph" role="img" aria-label="Red sport motorcycle on a road" style="background:linear-gradient(135deg,#8b2a22,#5a6a4a)"></div>
        <h6>Best Three Motorcycles for a Road Trip Around Thailand</h6><div class="date">2021-02-03</div>
        <p>Thailand is considered one of the world's best motorcycle touring destinations. The tropical landscape, palm trees, sun, temples and hidden waterfalls.</p><div class="more">Read more</div></article>
    </div>
  </section>

  <footer class="foot">
    <div class="logo"><span class="dot" style="width:18px;height:18px"></span>RIDE ON</div>
    <p class="blurb">Lorem ipsum is simply dummy text of the printing and typesetting industry. Lorem ipsum has been the industry's standard dummy text ever since the 1500s.</p>
    <ul><li>Home</li><li>Deliver</li><li>How It Works</li><li>Booking Process</li><li>Popular Bikes</li><li>Blogs</li></ul>
    <p class="copy">Copyright©2021 Ride On • Privacy Policy Site Map<br>Terms &amp; Conditions</p>
    <div class="socials"><span></span><span></span><span></span></div>
  </footer>
</main>

<!-- mobile homepage -->
<main class="page mob">
  <nav class="nav">
    <div class="logo"><span class="dot" style="width:9px;height:9px"></span>RIDE ON</div>
    <div class="right"><div class="socials"><span></span><span></span><span></span></div><div class="burger"></div></div>
  </nav>

  <section class="hero" role="img" aria-label="Row of rental motorbikes parked along a street, darkened">
    <h1>Fast Motorbike Rentals In Phuket, Thailand</h1>
    <ul>
      <li>Free Delivery &amp; Pick Up Anywhere In Phuket</li>
      <li>Free High Quality Helmet Included</li>
      <li>Free Unlimited Mileage</li>
      <li>Easy &amp; Quick Online Booking</li>
      <li>No Credit Card Required</li>
      <li>Pay When Bike Is Delivered</li>
      <li>Speak English &amp; Thai</li>
    </ul>
  </section>

  <form class="bookcard">
    <div class="steps"><span class="on">Step 1</span><span>Step 2</span><span>Step 3</span></div>
    <h3>Choose Your Bike</h3>
    <div class="select">Vendor &nbsp;&nbsp;&nbsp;&nbsp;&nbsp;&nbsp;&nbsp;&nbsp;&nbsp;&nbsp; ▾</div>
    <div class="bikeview">
      <div class="ph" role="img" aria-label="Blue scooter"></div>
      <span class="arrow" style="left:-4px">‹</span>
      <span class="arrow" style="right:-4px">›</span>
    </div>
    <h4>ENTER YOUR DETAILS</h4>
    <div class="fields">
      <div>Name</div><div>Phone Number</div>
      <div class="full">Email</div>
      <div class="full">Messaging ID</div>
      <div class="full area">Location</div>
    </div>
    <span class="btn">Next</span>
  </form>

  <div class="callbox"><b>You Can Call Us</b><span>123-456-7890</span></div>

  <h2 class="cities-h">We Deliver Motorbikes and Scooters To These Cities In Phuket, Thailand</h2>
  <div class="cities">
    <div class="city">Cherng Talay</div><div class="city">Bangtao</div><div class="city">Chalong</div><div class="city">Kamala</div>
    <div class="city">Karon</div><div class="city">Kata</div><div class="city">Kathu</div><div class="city">Nai Harn</div>
    <div class="city">Patong</div><div class="city">Phuket Town</div><div class="city">Rawai</div><div class="city">Mai Khao</div>
  </div>

  <section class="how">
    <h2 class="center-h">How It Works</h2>
    <div class="stack">
      <div class="step-card"><div class="ph" role="img" aria-label="Grey scooter parked on a street" style="background:linear-gradient(#8a9aa6,#3d4148)"></div><span class="num">1</span><p>Choose Your Bike</p></div>
      <div class="step-card"><div class="ph" role="img" aria-label="Hand signing a rental form" style="background:linear-gradient(135deg,#e9ecef,#9fb2c6)"></div><span class="num">2</span><p>Enter Rental Date Period &amp; Enter Delivery Address Or Choose To Pick Up</p></div>
      <div class="step-card"><div class="ph" role="img" aria-label="Two travellers riding a scooter" style="background:linear-gradient(135deg,#7f6b5a,#c8b9a6)"></div><span class="num">3</span><p>Get Your Bike Delivered In Less Than 2 Hours Or Pick Up ASAP!</p></div>
    </div>
  </section>

  <section class="bikes">
    <h2 class="center-h">Popular Bikes</h2>
    <div class="row">
      <div class="bike"><div class="frame"><div class="ph" role="img" aria-label="Grey and black scooter" style="background:radial-gradient(ellipse,#4b4f55 0%,#8a8f96 40%,rgba(255,255,255,0) 70%)"></div></div>
        <h5>Kito-Glide</h5><p>120 Km/H or 75 Mph<br>200 Baht/Day<br>58.8 km/L or 138 MPG</p><span class="btn">Booking</span></div>
      <div class="bike"><div class="frame"><div class="ph" role="img" aria-label="Blue scooter" style="background:radial-gradient(ellipse,#1f5fb3 0%,#5e8fd0 40%,rgba(255,255,255,0) 70%)"></div></div></div>
    </div>
  </section>

  <section class="news">
    <h2>Latest News &amp;<br>Blogs</h2>
    <div class="row">
      <article class="post"><div class="ph" role="img" aria-label="Riders on scooters at a checkpoint" style="background:linear-gradient(135deg,#6d7a5c,#b9b4a2)"></div>
        <h6>The Penalties for Traffic Offenses in Thailand</h6><div class="date">2021-02-03</div>
        <p>Many people riding in Thailand are not aware of the local traffic rules. Common offenses include riding without a helmet.</p><div class="more">Read more</div></article>
      <article class="post"><div class="ph" role="img" aria-label="Packing list items for a motorbike trip" style="background:linear-gradient(135deg,#d6e8f2,#4f9ad1)"></div>
        <h6>What to Take with You on a Motorcycle Trip</h6><div class="date">2021-02-03</div>
        <p>Renting a scooter is a popular way to explore.</p><div class="more">Read more</div></article>
    </div>
  </section>

  <footer class="foot">
    <div class="logo"><span class="dot" style="width:12px;height:12px"></span>RIDE ON</div>
    <p class="blurb">Lorem ipsum is simply dummy text of the printing and typesetting industry. Lorem ipsum has been the industry's standard dummy text ever since the 1500s.</p>
    <ul><li>Home</li><li>Deliver</li><li>How It Works</li><li>Booking Process</li><li>Popular Bikes</li><li>Blogs</li></ul>
    <p class="copy">Copyright©2021 Ride On • Privacy Policy Site<br>Map Terms &amp; Conditions</p>
    <div class="socials"><span></span><span></span><span></span></div>
  </footer>
</main>

</body>
</html>
```